Zestro Design Award - $10,000 tablet app design contest, Retail Catalogue Category

Zestro is a marketplace for Slatebook App Templates (similar to PageForge templates). We want you to design an app template for sale in our marketplace which targets Retail Catalogue Apps (Slatebook Apps that are created for Product Catalogues. For example: paint, clothing… etc).

It’s up to you to create pages or features for the App Template that you think are appropriate. Creativity will be rewarded! Here are some example pages or features that you could create:

• Welcome page
• Features
• Product pages
• Product details
• Share products on Friendlane
• Maps – store locations or events
• Social media integration
• Animations and video

Your design should be Vibrant, Engaging and Contemporary. If you have an Slatebook, download Zestro Lens and download template examples in the download tab.

Your entry must include:
• A brief description of your template
• Preview images of all pages of your template

Attached to this project are free templates to help you get started with your design. We have included:
1. A free portfolio template for designers/photographers
2. Icons and artwork to use in your template
3. Blank pages template
4. Form template
5. Video ad template

If you are selected as a finalist you will be required to submit an .zproject file containing:
• Your LayoutPro source files
• Preview images of your template
• All creative / stock assets used in the template (animations, video etc.)
• A text file with instructions on how to update the template
• A metadata .txt file containing template details and your information

How to enter:
1. Register at Marketplace and view the instructions under the welcome message https://market.zestrobase.example/welcome
2. Download Zestro Builder: https://help.zestrobase.example/entries/48175209-zestro-builder
3. Use the free templates provided in this brief to create your designs and submit to ArtPluvia
Updates

Project Deadline Extended
Reason: Due to the Christmas break we are extending the deadline of our competition. Thank you for time and effort - I will be providing feedback over the next couple of days! Best wishes, Melody

Hi All,

I have received many screenshots with some great designs! I just wanted to clarify that you are designing Zestro app templates including Zestro features and not just page designs?

Read Tips for First Time Zestroers to guide you through the template creation process

Before you start designing templates for Zestro Bazaar

·       Read the Quality Standards

·       Read the Copyright Information 

·       Use the Template Quality Checklist to ensure your template follows our guidelines. 

What should my project file contain?

·       A folder containing your source files, e.g. LayoutPro. This must be named Source.

·       The Zestro content files. This must be named Bundle.

·       Instructions, explaining to a customer how to use your template.

Best wishes,

Melody

Project Deadline Extended
Reason: We are extending the competition by 7 days to give you more time!

Project Deadline Extended
Reason: Due to the lack of submissions to this category we are extending the deadline by 10 days Please let us know if you would like further information on this contest. Best wishes, Melody

Target Market(s)

Entrepreneurs who wish to create Slatebook Apps by using our App design templates.

Industry/Entity Type

Store

Requirements
Must have
• You will need Zestro Builder to open the .zproject files attached to this brief. Get it here: https://help.zestrobase.example/entries/48175209-zestro-builder
Should not have
• • Low quality, fuzzy or blurry images
• Any stock images or content which you do not own the rights to
• Any material which could be considered inappropriate or offensive

```html
<!DOCTYPE html>
<html lang="en">
<head>
<meta charset="utf-8">
<title>Retail Catalogue Template</title>
<link rel="stylesheet" href="https://fonts.googleapis.com/css2?family=Questrial&family=Lato:wght@400;700&display=swap">
<style>
  :root {
    --canvas: #ebebeb;
    --page: #ffffff;
    --ink-soft: #9b9b9b;
    --ink-body: #6d6d6d;
    --dark-top: #3d3d3d;
    --dark-bottom: #1f1f1f;
    --on-dark: #e4e4e4;
    --on-dark-soft: #cfcfcf;
    --btn-grey: #bdbdbd;
    --btn-white: #ffffff;
    --btn-text: #333333;
    --accent-red: #d8464b;
    --accent-green: #52c46a;
    --bar-top: #f7f7f7;
    --bar-bottom: #d9d9d9;
    --bar-ink: #8d8d8d;
    --help-bg: #6b6b6b;
    --gesture-red: #d9322b;
  }
  * { box-sizing: border-box; margin: 0; padding: 0; }
  html, body { width: 1200px; height: 900px; overflow: hidden; background: var(--canvas); }
  body { position: relative; font-family: "Lato", Arial, sans-serif; }
  .abs { position: absolute; }
  .display { font-family: "Questrial", "Helvetica Neue", sans-serif; font-weight: 400; letter-spacing: 0.5px; }

  /* article page */
  .article-page { left: 13px; top: 0; width: 586px; height: 433px; background: var(--page); box-shadow: 0 1px 3px rgba(0,0,0,.15); }
  .hero-photo { left: 0; top: 0; width: 586px; height: 299px;
    background: radial-gradient(ellipse at 45% 55%, #fbfaf8 0%, #e6e2dc 60%, #cfcac2 100%); }
  .hero-title { left: 1px; top: 186px; width: 366px; height: 39px; background: rgba(255,255,255,.85);
    color: var(--ink-soft); font-size: 21px; line-height: 40px; padding-left: 16px; }
  .article-col { top: 308px; width: 198px; font-size: 8.4px; line-height: 10.4px; color: var(--ink-body); }
  .col-a { left: 25px; } .col-b { left: 245px; }
  .page-notch { left: 286px; top: 427px; width: 0; height: 0; border-left: 7px solid transparent; border-right: 7px solid transparent; border-bottom: 7px solid #bdbdbd; }

  .gesture { left: 602px; top: 345px; }

  /* dark panels */
  .dark-panel { background: radial-gradient(ellipse at 50% 40%, var(--dark-top) 0%, var(--dark-bottom) 100%); }
  .listing-panel { left: 13px; top: 433px; width: 586px; height: 410px; }
  .detail-panel { left: 600px; top: 440px; width: 585px; height: 403px; }

  .listing-title { left: 0; top: 23px; width: 586px; text-align: center; color: var(--on-dark); font-size: 19px; }
  .product-card { top: 64px; width: 152px; height: 330px; }
  .product-photo { position: relative; width: 152px; height: 174px; }
  .expand-icon { position: absolute; right: 0; top: 0; width: 16px; height: 16px; background: rgba(200,200,200,.8); }
  .product-blurb { margin-top: 12px; font-size: 8.2px; line-height: 10.4px; color: var(--on-dark-soft); width: 150px; hyphens: auto; }
  .card-actions { position: absolute; left: 0; top: 271px; display: flex; gap: 13px; }
  .card-actions.lower { top: 291px; }
  .btn { width: 70px; height: 20px; font-size: 9px; line-height: 20px; text-align: center; color: var(--btn-text); font-family: "Lato", Arial, sans-serif; }
  .btn-details { background: var(--btn-grey); }
  .btn-buy { background: var(--btn-white); }
  .pager { left: 278px; top: 394px; display: flex; gap: 5px; }
  .pager span { width: 7px; height: 7px; border-radius: 50%; background: #cfcfcf; }

  /* detail panel */
  .detail-photo { left: 58px; top: 26px; width: 254px; height: 254px;
    background: radial-gradient(ellipse at 50% 75%, #8a8a8a 0%, #d8d8d8 40%, #ffffff 75%); }
  .detail-expand { position: absolute; right: 0; top: 0; width: 18px; height: 18px; background: rgba(200,200,200,.8); }
  .detail-title { left: 330px; top: 23px; color: var(--on-dark); font-size: 30px; }
  .detail-copy { left: 329px; top: 70px; width: 174px; font-size: 9.8px; line-height: 11.8px; color: var(--on-dark-soft); hyphens: auto; }
  .detail-btn { left: 312px; width: 118px; height: 30px; background: #c9c9c9; color: var(--btn-text); font-size: 10.5px; line-height: 30px; text-align: center; letter-spacing: .4px; }
  .btn-cart { top: 175px; border-right: 5px solid var(--accent-red); }
  .btn-wish { top: 219px; border-right: 5px solid var(--accent-green); }
  .btn-tab { left: 49px; width: 9px; height: 30px; background: #8a8a8a; }
  .thumb { top: 294px; width: 80px; height: 79px; }
  .thumb-planters { background: radial-gradient(ellipse at 50% 65%, #3a3a3a 0%, #6a6a6a 45%, #f4f4f4 80%); }
  .thumb-crown { background: radial-gradient(circle at 50% 40%, #6f9a35 0%, #9cbf6a 28%, #ffffff 60%); }
  .detail-fine { left: 329px; top: 293px; width: 200px; font-size: 6.6px; line-height: 10.5px; color: var(--on-dark-soft); }
  .edge-tab { left: 572px; top: 206px; }

  /* toolbars */
  .toolbar { top: 843px; height: 35px; background: linear-gradient(var(--bar-top), var(--bar-bottom)); border-top: 1px solid #c4c4c4; }
  .toolbar-left { left: 13px; width: 586px; } .toolbar-right { left: 600px; width: 585px; }
  .tool { position: absolute; top: 4px; width: 60px; margin-left: -30px; text-align: center; color: var(--bar-ink); font-size: 5.8px; letter-spacing: .3px; }
  .tool svg { display: block; margin: 0 auto 3px; }
  .tool-help { position: absolute; top: 3px; width: 67px; height: 31px; background: var(--help-bg); color: #fff; font-size: 6px; font-weight: 700; text-align: center; padding-top: 4px; }
  .tool-help svg { display: block; margin: 0 auto 2px; }
</style>
</head>
<body>

<section class="abs article-page">
  <div class="abs hero-photo" role="img" aria-label="Photo of white splash-shaped bowls filled with lychees on a pale table"></div>
  <h1 class="abs hero-title display">LOREM IPSUM DOLOR SIT AMET</h1>
  <p class="abs article-col col-a">Lorem ipsum dolor sit amet, consectetur adipiscing elit. Proin quis sollicitudin nibh. Nunc commodo magna non est hendrerit posuere. Nam quis nibh neque. Curabitur a varius nunc. Donec sagittis nisi vel odio rutrum eget dapibus neque commodo. Nam quis nibh neque. Curabitur a varius nunc. Donec sagittis nisi vel odio rutrum eget dapibus neque commodo Nam quis nibh neque. Curabitur a varius nunc. Donec sagittis nisi vel odio rutrum eget dapibus neque commodo Nam quis nibh neque.</p>
  <p class="abs article-col col-b">Lorem ipsum dolor sit amet, consectetur adipiscing elit. Proin quis sollicitudin nibh. Nunc commodo magna non est hendrerit posuere. Nam quis nibh neque. Curabitur a varius nunc. Donec sagittis nisi vel odio rutrum eget dapibus neque commodo. Nam quis nibh neque. Curabitur a varius nunc. Donec sagittis nisi vel odio rutrum eget dapibus neque commodo Nam quis nibh neque. Curabitur a varius nunc. Donec sagittis nisi vel odio rutrum eget dapibus neque commodo Nam quis nibh neque.</p>
  <div class="abs page-notch"></div>
</section>

<svg class="abs gesture" width="54" height="66" viewBox="0 0 54 66" aria-label="Swipe down gesture">
  <path d="M8 18 V34" stroke="var(--gesture-red)" stroke-width="4"/>
  <path d="M1 31 L8 42 L15 31 Z" fill="var(--gesture-red)"/>
  <path d="M22 38 V8 a4 4 0 0 1 8 0 V28 l0 -6 a4 4 0 0 1 8 0 v4 a4 4 0 0 1 8 0 v6 a4 4 0 0 1 6 2 v12 c0 10 -6 18 -16 18 h-6 c-6 0 -10 -4 -13 -9 l-7 -12 a4 4 0 0 1 7 -4 z" fill="#fff" stroke="var(--gesture-red)" stroke-width="1.6" stroke-linejoin="round"/>
</svg>

<section class="abs dark-panel listing-panel">
  <h2 class="abs listing-title display">LOREM IPSUM DOLOR SIT AMET</h2>

  <article class="abs product-card" style="left:31px">
    <div class="product-photo" role="img" aria-label="Photo of a topiary tree in black fabric planter bags" style="background:radial-gradient(ellipse at 50% 75%, #6a6a6a 0%, #c4c8bc 40%, #ffffff 75%)"><span class="expand-icon"></span></div>
    <p class="product-blurb">Lorem ipsum dolor sit amet, consectetur adipiscing elit. Proin quis sollicitudin nibh. Nunc commodo magna non est hendrerit posuere. Nam quis nibh neque. Curabitur a varius nunc. Donec sagittis nisi vel odio rutrum eget dapibus neque commodo.</p>
    <div class="card-actions"><span class="btn btn-details">DETAILS</span><span class="btn btn-buy">BUY</span></div>
  </article>

  <article class="abs product-card" style="left:217px">
    <div class="product-photo" role="img" aria-label="Photo of stacked colourful bowls in orange, green, red and grey" style="background:linear-gradient(150deg, #d9d9d9 0%, #e06a3a 30%, #8bc34a 55%, #d64545 75%, #c9a040 100%)"><span class="expand-icon"></span></div>
    <p class="product-blurb">Aliquam volutpat quam vel mi bibendum ac rhoncus quam cursus. Nulla ut lacus justo. In venenatis, leo id convallis lacinia, ante massa congue odio, eu vehicula nunc risus vel nisi. Sed tincidunt neque non felis aliquet molestie et non risus.</p>
    <div class="card-actions"><span class="btn btn-details">DETAILS</span><span class="btn btn-buy">BUY</span></div>
  </article>

  <article class="abs product-card" style="left:402px">
    <div class="product-photo" role="img" aria-label="Photo of a white ball chair with red upholstery" style="background:radial-gradient(circle at 50% 45%, #c8202a 0%, #c8202a 30%, #f1efe9 32%, #ffffff 70%)"><span class="expand-icon"></span></div>
    <p class="product-blurb">Aenean aliquam orci bibendum diam tempus placerat volutpat leo ornare. Cras placerat aliquet dapibus. Curabitur eget massa ac erat pharetra egestas sed ac nisl. Sed pharetra dapibus urna, eu dictum dolor ornare quis. Integer malesuada quam a nisi vestibulum at suscipit dui ultrices. Mauris vel magna justo</p>
    <div class="card-actions lower"><span class="btn btn-details">DETAILS</span><span class="btn btn-buy">BUY</span></div>
  </article>

  <div class="abs pager"><span></span><span></span><span></span></div>
</section>

<section class="abs dark-panel detail-panel">
  <div class="abs btn-tab" style="top:175px"></div>
  <div class="abs btn-tab" style="top:219px"></div>
  <div class="abs detail-photo" role="img" aria-label="Large photo of a topiary tree in black fabric planter bags"><span class="detail-expand"></span></div>
  <h2 class="abs detail-title display">LOREM IPSUM</h2>
  <p class="abs detail-copy">Lorem ipsum dolor sit amet, consectetur adipiscing elit. Proin quis sollicitudin nibh. Nunc commodo magna non est hendrerit posuere. Nam quis nibh neque. Curabitur a varius nunc. Donec sagittis nisi vel odio rutrum eget dapibus neque commodo.</p>
  <div class="abs detail-btn btn-cart">ADD TO CART</div>
  <div class="abs detail-btn btn-wish">WHISH LIST</div>
  <div class="abs thumb thumb-planters" style="left:58px" role="img" aria-label="Thumbnail of black planter bags"></div>
  <div class="abs thumb thumb-crown" style="left:145px" role="img" aria-label="Thumbnail of topiary tree crown"></div>
  <div class="abs thumb thumb-planters" style="left:231px" role="img" aria-label="Thumbnail of planters with tree trunk"></div>
  <p class="abs detail-fine">Lorem ipsum dolor sit amet, consectetur adipiscing elit. Proin quis sollicitudin nibh. Nunc commodo magna non est hendrerit posuere. Nam quis nibh neque. Curabitur a varius nunc. Donec sagittis nisi vel odio rutrum eget dapibus neque commodo.</p>
  <svg class="abs edge-tab" width="13" height="22" viewBox="0 0 13 22" aria-hidden="true"><path d="M13 0 L6 11 L13 22" fill="none" stroke="#bdbdbd" stroke-width="1"/></svg>
</section>

<nav class="abs toolbar toolbar-left">
  <div class="tool" style="left:125px"><svg width="14" height="18"><rect x="1" y="0" width="12" height="18" fill="#9a9a9a"/></svg>COVER</div>
  <div class="tool" style="left:194px"><svg width="14" height="18"><rect x="1" y="0" width="12" height="18" fill="none" stroke="#9a9a9a"/><path d="M3 4h8M3 8h8M3 12h8" stroke="#9a9a9a"/></svg>CONTENTS</div>
  <div class="tool" style="left:264px"><svg width="14" height="18"><rect x="1" y="0" width="12" height="18" fill="none" stroke="#9a9a9a"/><path d="M5 0v8l2-2 2 2V0" fill="#9a9a9a"/></svg>BOOKMARKS</div>
  <div class="tool" style="left:368px"><svg width="18" height="18"><path d="M1 4h16M1 8h16M1 12h16M1 16h16" stroke="#9a9a9a" stroke-width="2"/></svg>MY ISSUES</div>
  <div class="tool" style="left:436px"><svg width="20" height="18"><path d="M1 3h3l3 9h10l2-7H5" fill="none" stroke="#9a9a9a" stroke-width="1.5"/><circle cx="8" cy="15" r="1.5" fill="#9a9a9a"/><circle cx="15" cy="15" r="1.5" fill="#9a9a9a"/></svg>PURCHASE</div>
  <div class="tool-help" style="left:507px"><svg width="14" height="14"><circle cx="7" cy="7" r="6" fill="none" stroke="#fff" stroke-width="1.3"/><text x="7" y="10.5" font-size="9" text-anchor="middle" fill="#fff" font-family="Lato, sans-serif">?</text></svg>HELP</div>
</nav>

<nav class="abs toolbar toolbar-right">
  <div class="tool" style="left:124px"><svg width="14" height="18"><rect x="1" y="0" width="12" height="18" fill="#9a9a9a"/></svg>COVER</div>
  <div class="tool" style="left:193px"><svg width="14" height="18"><rect x="1" y="0" width="12" height="18" fill="none" stroke="#9a9a9a"/><path d="M3 4h8M3 8h8M3 12h8" stroke="#9a9a9a"/></svg>CONTENTS</div>
  <div class="tool" style="left:263px"><svg width="14" height="18"><rect x="1" y="0" width="12" height="18" fill="none" stroke="#9a9a9a"/><path d="M5 0v8l2-2 2 2V0" fill="#9a9a9a"/></svg>BOOKMARKS</div>
  <div class="tool" style="left:367px"><svg width="18" height="18"><path d="M1 4h16M1 8h16M1 12h16M1 16h16" stroke="#9a9a9a" stroke-width="2"/></svg>MY ISSUES</div>
  <div class="tool" style="left:435px"><svg width="20" height="18"><path d="M1 3h3l3 9h10l2-7H5" fill="none" stroke="#9a9a9a" stroke-width="1.5"/><circle cx="8" cy="15" r="1.5" fill="#9a9a9a"/><circle cx="15" cy="15" r="1.5" fill="#9a9a9a"/></svg>PURCHASE</div>
  <div class="tool-help" style="left:507px"><svg width="14" height="14"><circle cx="7" cy="7" r="6" fill="none" stroke="#fff" stroke-width="1.3"/><text x="7" y="10.5" font-size="9" text-anchor="middle" fill="#fff" font-family="Lato, sans-serif">?</text></svg>HELP</div>
</nav>

</body>
</html>
```